German Headhunter/ HR Consultancy needs Business Cards Design

We need a business Card Design for our Company in Stuttgart. We are specialized as Headhunter/ HR Consultancy in Placement of specialist and managers in permanent employment. Please refer to our business logo.

```html
<!DOCTYPE html>
<html lang="en">
<head>
<meta charset="utf-8">
<title>Kernwerk Personalberatung – Business Cards</title>
<link rel="stylesheet" href="https://fonts.googleapis.com/css2?family=Montserrat:wght@500;700;800&family=Arimo:wght@400&display=swap">
<style>
  :root {
    --brand-blue: #3b56a8;
    --ink: #1d1d22;
    --grey: #9a9ca3;
    --line-grey: #b8b9bd;
    --paper: #ffffff;
    --backdrop: #e9eaee;
  }
  * { box-sizing: border-box; margin: 0; padding: 0; }
  html, body { width: 1200px; height: 948px; overflow: hidden; }
  body {
    background: var(--backdrop);
    display: flex;
    flex-direction: column;
    align-items: center;
    justify-content: center;
    gap: 56px;
  }
  .card {
    position: relative;
    width: 640px;
    height: 366px;
    border-radius: 22px;
    overflow: hidden;
    box-shadow: 0 10px 30px rgba(20, 24, 40, 0.18);
  }

  /* Shared wordmark */
  .wordmark {
    display: flex;
    align-items: center;
    font-family: "Montserrat", sans-serif;
    font-weight: 700;
    letter-spacing: 0.04em;
    text-transform: uppercase;
    white-space: nowrap;
  }
  .wordmark-square { flex: none; }

  /* Front */
  .card-front {
    background: var(--brand-blue);
    display: flex;
    align-items: center;
    justify-content: center;
  }
  .card-front .wordmark { color: var(--paper); font-size: 23px; gap: 14px; }
  .card-front .wordmark-square { background: var(--paper); width: 28px; height: 28px; }

  /* Back */
  .card-back { background: var(--paper); }
  .card-back .wordmark {
    position: absolute;
    left: 40px;
    top: 188px;
    color: var(--brand-blue);
    font-size: 13px;
    gap: 9px;
  }
  .card-back .wordmark-square { background: var(--brand-blue); width: 18px; height: 18px; }
  .divider {
    position: absolute;
    left: 366px;
    top: 70px;
    width: 1px;
    height: 190px;
    background: var(--line-grey);
  }
  .contact {
    position: absolute;
    left: 392px;
    top: 74px;
    color: var(--ink);
    font-family: "Arimo", Arial, sans-serif;
  }
  .contact-name {
    font-family: "Montserrat", sans-serif;
    font-weight: 800;
    font-size: 22px;
    color: var(--brand-blue);
    letter-spacing: 0.02em;
  }
  .contact-role { font-size: 14px; margin-top: 2px; margin-bottom: 16px; }
  .contact-list { list-style: none; font-size: 13.5px; line-height: 1.75; }
  .contact-list li { display: flex; align-items: center; gap: 8px; }
  .contact-list svg { width: 11px; height: 11px; fill: var(--brand-blue); flex: none; }
  .contact-address { font-size: 13.5px; line-height: 1.45; margin-top: 10px; }
  .edge-bands { position: absolute; left: 0; bottom: 0; width: 640px; height: 40px; }
</style>
</head>
<body>

<section class="card card-front" aria-label="Business card front">
  <div class="wordmark">
    <span class="wordmark-square"></span>
    <span class="wordmark-name">Kernwerk Personalberatung</span>
  </div>
</section>

<section class="card card-back" aria-label="Business card back">
  <div class="wordmark">
    <span class="wordmark-square"></span>
    <span class="wordmark-name">Kernwerk Personalberatung</span>
  </div>

  <div class="divider"></div>

  <div class="contact">
    <p class="contact-name">JONAS KELLER</p>
    <p class="contact-role">CEO/Founder</p>
    <ul class="contact-list">
      <li>
        <svg viewBox="0 0 24 24" aria-hidden="true"><path d="M6.6 10.8a15.1 15.1 0 0 0 6.6 6.6l2.2-2.2a1 1 0 0 1 1-.25 11.4 11.4 0 0 0 3.6.57 1 1 0 0 1 1 1V20a1 1 0 0 1-1 1A17 17 0 0 1 3 4a1 1 0 0 1 1-1h3.5a1 1 0 0 1 1 1c0 1.25.2 2.45.57 3.57a1 1 0 0 1-.25 1z"/></svg>
        (555) 010 - 2834
      </li>
      <li>
        <svg viewBox="0 0 24 24" aria-hidden="true"><path d="M2 5h20v14H2z M2 5l10 8 10-8" fill="none" stroke="#3b56a8" stroke-width="3"/></svg>
        info@kernwerkpersonal.com
      </li>
      <li>
        <svg viewBox="0 0 24 24" aria-hidden="true"><circle cx="12" cy="12" r="10"/></svg>
        www.kernwerkpersonal.com
      </li>
    </ul>
    <p class="contact-address">22 Lindenweg Road<br>Ste C Country Name, 7010</p>
  </div>

  <svg class="edge-bands" viewBox="0 0 640 40" preserveAspectRatio="none" aria-hidden="true">
    <polygon points="0,34 400,34 390,40 0,40" fill="#3b56a8"/>
    <polygon points="404,22 640,22 640,40 394,40" fill="#9a9ca3"/>
  </svg>
</section>

</body>
</html>
```